Cool Website Design Bright Coat Studio.

We need a new website, using our existing domain, with a similar function to https://www.plomfilmworks.com/ or https://www.trexafoilcraft.com/ instagram bright_coat.studio.
We can send google docs with pictures.
Logo attached

```html
<!DOCTYPE html>
<html lang="en">
<head>
<meta charset="utf-8">
<title>Bright Coat Studio — Homepage</title>
<link rel="stylesheet" href="https://fonts.googleapis.com/css2?family=Poppins:wght@400;500;600;700;800&display=swap">
<style>
:root{
  --ink:#0e0e10;
  --ink-2:#18181b;
  --ink-3:#1e1e22;
  --white:#ffffff;
  --muted:#b9b9c2;
  --purple:#7a3fd9;
  --violet:#6a4ee6;
  --blue:#2f8ae8;
  --blue-2:#3b9af0;
  --line:rgba(255,255,255,.55);
  --grad:linear-gradient(100deg,#7a3fd9 0%,#4f6ae6 55%,#2f8ae8 100%);
}
*{box-sizing:border-box;margin:0;padding:0}
html,body{width:1200px;height:3904px;overflow:hidden;background:var(--ink)}
body{font-family:'Poppins',sans-serif;color:var(--white);position:relative}
.section{position:relative;width:1200px;overflow:hidden}
.abs{position:absolute}

/* header */
.site-header{height:118px;background:var(--ink)}
.brand{left:148px;top:24px;font-weight:700;font-size:19px;line-height:1.15;color:var(--violet);letter-spacing:.5px;display:flex;align-items:center;gap:10px}
.brand .mark{width:22px;height:22px;background:var(--violet);border-radius:4px;flex:none}
.topline{left:324px;top:22px;display:flex;gap:18px;font-size:11.5px;color:#e5e5ea;align-items:center}
.topline span{display:flex;align-items:center;gap:6px}
.nav{left:324px;top:64px;display:flex;gap:32px;font-size:15px;font-weight:500}
.nav .caret{color:var(--blue-2);font-size:10px;margin-left:4px}
.quote-btn{left:899px;top:57px;width:151px;height:42px;border-radius:21px;background:var(--grad);display:flex;align-items:center;justify-content:center;font-size:15px;font-weight:500}

/* hero */
.hero{height:608px;background:radial-gradient(ellipse at 35% 55%,#2a2520 0%,#141313 55%,#0c0c0d 100%)}
.hero-title{left:148px;top:104px;font-size:32px;font-weight:800;line-height:38px;text-transform:uppercase}
.hero-title .c-blue{color:var(--blue-2)}
.hero-title .c-purple{color:var(--violet)}
.hero-copy{left:148px;top:270px;width:420px;font-size:14px;line-height:24px;color:var(--muted)}
.btn{display:flex;align-items:center;justify-content:center;border-radius:22px;font-size:14px;font-weight:500}
.hero-btn{left:148px;top:370px;width:152px;height:42px;background:linear-gradient(90deg,#6a4ee6,#4f6ae6)}
.partners{left:148px;top:526px;display:flex;gap:16px;align-items:center}
.partners i{display:block;height:14px;background:#d9d9de;border-radius:3px}
.hero-grid{left:761px;top:0;width:439px;display:grid;grid-template-columns:208px 208px;grid-auto-rows:196px;gap:10px 12px}
.shot{border-radius:6px;border:1px solid #2c2c30}
.s1{background:linear-gradient(160deg,#5c6770,#2c3035)}
.s2{background:linear-gradient(160deg,#9a9ca6,#4c4d55)}
.s3{background:linear-gradient(160deg,#c85a2b,#3d3f8c)}
.s4{background:linear-gradient(160deg,#4666e6,#1f2fa8)}
.s5{background:linear-gradient(160deg,#a83240,#3a2a35)}
.s6{background:linear-gradient(160deg,#4a7a3a,#6a54c8)}

/* services */
.services{height:222px;display:grid;grid-template-columns:repeat(4,300px)}
.svc{position:relative;padding:0 16px}
.svc-1{background:linear-gradient(135deg,#3a7ee8,#6a52e0)}
.svc-2{background:linear-gradient(135deg,#6a4ee0,#7a3fd9)}
.svc-3{background:linear-gradient(135deg,#4a68e4,#2f8ae8)}
.svc-4{background:linear-gradient(135deg,#7a42da,#3a84ea)}
.svc svg.hex{position:absolute;left:24px;top:34px}
.svc-name{position:absolute;left:16px;bottom:28px;font-size:18px}
.svc-arrow{position:absolute;right:18px;bottom:26px}

/* about */
.about{height:514px;background:var(--ink)}
.about h2{left:148px;top:90px;font-size:32px;font-weight:700}
.about-copy{left:148px;top:148px;width:488px;font-size:12.5px;line-height:20px;color:#e2e2e8;text-align:justify}
.about-art{left:684px;top:50px;width:360px;height:380px;border-radius:50%;background:linear-gradient(120deg,#dfe6ee 0%,#8db8e4 45%,#2c2c30 100%)}

/* tagline */
.tagline{height:266px;background:var(--ink-3)}
.tagline h2{left:148px;top:84px;font-size:32px;font-weight:700;line-height:43px}
.tagline p{left:647px;top:88px;width:401px;font-size:12.5px;line-height:20px;color:#e2e2e8;text-align:justify}
.tagline p em{font-style:normal;color:var(--blue-2)}

/* promo */
.promo{height:401px;background:var(--grad);overflow:visible;z-index:2}
.promo h2{left:0;width:1200px;top:48px;text-align:center;font-size:31px;font-weight:700;line-height:43px}
.promo-btn{left:529px;top:150px;width:142px;height:40px;background:#1a1a1d;color:#fff}
.promo-art{left:290px;top:215px;width:620px;height:290px;border-radius:10px;background:linear-gradient(180deg,rgba(220,220,224,.35) 0%,rgba(150,40,50,.55) 60%,rgba(30,30,34,.6) 100%)}

/* gallery */
.gallery{height:746px;background:var(--ink-3);z-index:1}
.gallery h2{left:0;width:1200px;top:132px;text-align:center;font-size:32px;font-weight:700}
.gallery-grid{left:148px;top:200px;display:grid;grid-template-columns:repeat(4,216px);grid-auto-rows:186px;gap:12px 12px}
.g1{background:linear-gradient(150deg,#4a5a6e,#2a2f36)}
.g2{background:linear-gradient(150deg,#8f939a,#3a3e46)}
.g3{background:linear-gradient(150deg,#6e5a8a,#34364a)}
.g4{background:linear-gradient(150deg,#8a7a70,#1d1e22)}
.g5{background:linear-gradient(150deg,#f0f0f2,#9aa4b6)}
.g6{background:linear-gradient(150deg,#2f7a3a,#2a4aa0)}
.g7{background:linear-gradient(150deg,#3a3d44,#131416)}
.g8{background:linear-gradient(150deg,#5a6474,#1a1c20)}

/* contact */
.contact{height:666px;background:linear-gradient(160deg,#2a2c4a 0%,#171a2c 60%,#141418 100%)}
.contact-card{left:148px;top:110px;width:902px;height:430px;border-radius:14px;background:linear-gradient(110deg,#7a3fd9 0%,#5560e6 55%,#2f8ae8 100%)}
.contact-card h2{position:absolute;left:36px;top:36px;font-size:32px;font-weight:700}
.field{position:absolute;font-size:13px;color:#f0f0f5;border-bottom:1px solid var(--line);padding-bottom:8px}
.send-btn{position:absolute;left:38px;top:360px;width:152px;height:40px;background:#1a1a1d}
.contact-photo{position:absolute;left:576px;top:38px;width:307px;height:358px;border-radius:10px;background:linear-gradient(150deg,#3a2f2a 0%,#7a6048 45%,#2a3a6a 100%)}

/* footer */
.site-footer{height:360px;background:var(--ink-2)}
.footer-brand{left:148px;top:66px}
.socials{left:148px;top:160px;display:flex;gap:10px}
.socials i{width:30px;height:30px;border-radius:50%;border:1.5px solid var(--violet);display:block}
.copy{left:148px;top:254px;font-size:11px;color:#a9a9b2}
.fcol{top:64px}
.fcol h3{font-size:14px;font-weight:600;color:var(--blue-2);margin-bottom:12px}
.fcol li{list-style:none;font-size:11px;line-height:24px;color:#c7c7cf}
.fcol li.ico{display:flex;gap:8px;align-items:flex-start;line-height:17px;margin-bottom:10px}
</style>
</head>
<body>

<header class="section site-header">
  <div class="abs brand"><span class="mark"></span><span>BRIGHT COAT<br>STUDIO</span></div>
  <div class="abs topline">
    <span><svg width="10" height="13" viewBox="0 0 10 13"><path d="M5 0a5 5 0 0 1 5 5c0 3.5-5 8-5 8S0 8.5 0 5a5 5 0 0 1 5-5z" fill="#3b9af0"/><circle cx="5" cy="5" r="1.8" fill="#0e0e10"/></svg>12 Lantern Row, Fenwick Park, Ostrava Bay</span>
    <span><svg width="13" height="10" viewBox="0 0 13 10"><rect width="13" height="10" rx="1.5" fill="#6a4ee6"/><path d="M1 1.5l5.5 4 5.5-4" stroke="#fff" stroke-width="1.2" fill="none"/></svg>info@brightcoatstudio.com</span>
    <span><svg width="12" height="12" viewBox="0 0 12 12"><path d="M2.5 0.5l2 2.5-1.2 1.5a7 7 0 0 0 4.2 4.2L9 7.5l2.5 2-1.2 2C5 11.5.5 7 .5 1.7z" fill="#3b9af0"/></svg>+800-5210-3388</span>
  </div>
  <nav class="abs nav">
    <span>About</span><span>Services<span class="caret">▾</span></span><span>Promotions<span class="caret">▾</span></span><span>Gallery</span><span>Contact Us</span>
  </nav>
  <div class="abs quote-btn">Get a quote</div>
</header>

<section class="section hero">
  <h1 class="abs hero-title">Protect your paint or<br>change your <span class="c-blue">colour</span><br><span class="c-purple">without</span> breaking<br>the bank.</h1>
  <p class="abs hero-copy">Lorem Ipsum is simply dummy text of the printing and typesetting industry. Lorem Ipsum has been the industry's standard dummy text ever</p>
  <div class="abs btn hero-btn">Book Now</div>
  <div class="abs partners" aria-label="Partner film brands">
    <i style="width:38px"></i><i style="width:50px"></i><i style="width:40px"></i><i style="width:34px"></i><i style="width:40px"></i><i style="width:40px"></i><i style="width:36px"></i>
  </div>
  <div class="abs hero-grid">
    <div class="shot s1" role="img" aria-label="Grey sports car with satin wrap in a parking garage"></div>
    <div class="shot s2" role="img" aria-label="Close-up of a wrapped tail light"></div>
    <div class="shot s3" role="img" aria-label="Car with a colourful graphic wrap"></div>
    <div class="shot s4" role="img" aria-label="Installer applying blue vinyl to a car panel"></div>
    <div class="shot s5" role="img" aria-label="Close-up of a red race number decal"></div>
    <div class="shot s6" role="img" aria-label="Car with a printed livery parked on grass"></div>
  </div>
</section>

<section class="section services">
  <div class="svc svc-1">
    <svg class="hex" width="90" height="100" viewBox="0 0 90 100"><path d="M45 2l41 23v50L45 98 4 75V25z" fill="none" stroke="#fff" stroke-width="2"/><rect x="28" y="38" width="34" height="24" rx="3" fill="none" stroke="#fff" stroke-width="2"/><path d="M36 38v-6h18v6M32 70h26" stroke="#fff" stroke-width="2" fill="none"/></svg>
    <span class="svc-name">Paint Protection Film</span>
    <svg class="svc-arrow" width="26" height="26" viewBox="0 0 26 26"><circle cx="13" cy="13" r="12" fill="none" stroke="#fff" stroke-width="1.3"/><path d="M9 17l8-8M11 9h6v6" stroke="#fff" stroke-width="1.3" fill="none"/></svg>
  </div>
  <div class="svc svc-2">
    <svg class="hex" width="90" height="100" viewBox="0 0 90 100"><path d="M45 2l41 23v50L45 98 4 75V25z" fill="none" stroke="#fff" stroke-width="2"/><path d="M22 62V44l8-10h30l8 10v18z" fill="none" stroke="#fff" stroke-width="2"/><circle cx="32" cy="63" r="5" fill="none" stroke="#fff" stroke-width="2"/><circle cx="58" cy="63" r="5" fill="none" stroke="#fff" stroke-width="2"/></svg>
    <span class="svc-name">Vinyl Wraps</span>
    <svg class="svc-arrow" width="26" height="26" viewBox="0 0 26 26"><circle cx="13" cy="13" r="12" fill="none" stroke="#fff" stroke-width="1.3"/><path d="M9 17l8-8M11 9h6v6" stroke="#fff" stroke-width="1.3" fill="none"/></svg>
  </div>
  <div class="svc svc-3">
    <svg class="hex" width="90" height="100" viewBox="0 0 90 100"><path d="M45 2l41 23v50L45 98 4 75V25z" fill="none" stroke="#fff" stroke-width="2"/><rect x="30" y="36" width="30" height="32" rx="3" fill="none" stroke="#fff" stroke-width="2"/><path d="M30 56h30M40 36v-6h10v6" stroke="#fff" stroke-width="2" fill="none"/></svg>
    <span class="svc-name">Window Tinting</span>
    <svg class="svc-arrow" width="26" height="26" viewBox="0 0 26 26"><circle cx="13" cy="13" r="12" fill="none" stroke="#fff" stroke-width="1.3"/><path d="M9 17l8-8M11 9h6v6" stroke="#fff" stroke-width="1.3" fill="none"/></svg>
  </div>
  <div class="svc svc-4">
    <svg class="hex" width="90" height="100" viewBox="0 0 90 100"><path d="M45 2l41 23v50L45 98 4 75V25z" fill="none" stroke="#fff" stroke-width="2"/><rect x="26" y="30" width="38" height="40" rx="4" fill="none" stroke="#fff" stroke-width="2"/><circle cx="36" cy="40" r="4" fill="none" stroke="#fff" stroke-width="2"/><circle cx="36" cy="52" r="4" fill="none" stroke="#fff" stroke-width="2"/><circle cx="36" cy="62" r="3" fill="none" stroke="#fff" stroke-width="2"/><rect x="48" y="36" width="8" height="28" rx="3" fill="none" stroke="#fff" stroke-width="2"/></svg>
    <span class="svc-name">Coloured PPF</span>
    <svg class="svc-arrow" width="26" height="26" viewBox="0 0 26 26"><circle cx="13" cy="13" r="12" fill="none" stroke="#fff" stroke-width="1.3"/><path d="M9 17l8-8M11 9h6v6" stroke="#fff" stroke-width="1.3" fill="none"/></svg>
  </div>
</section>

<section class="section about">
  <h2 class="abs">ABOUT US</h2>
  <p class="abs about-copy">Bright Coat Studio, a champion custom wrap shop in Fenwick Park. We specialize in vehicle wraps, efficiently producing quality designs for a flawless install. Our business is looked at like a fine art aside from a trade. Not only do we offer the best vinyl wraps, murals, and signage on the block, we have Kestrel Print Works as a bonus component for our clients. This division offers our clients a one-stop-shop for any items they might need printed or embroidered. Our staff walks you through all of the possibilities and choices so you can be assured your money is well spent. Bright Coat Studio is laser-focused from concept to finished product. It's not just about an unforgettable look, it's about recognizing the culture of your brand. For us, every new client is our next long-lasting relationship.</p>
  <div class="abs about-art" role="img" aria-label="Collage of a light blue wrapped sports car front and a hand applying film"></div>
</section>

<section class="section tagline">
  <h2 class="abs">BRIGHT COAT STUDIO<br>WE MAKE CARS BOLDER</h2>
  <p class="abs">As a nationally recognized company, Bright Coat Studio is known for its exceptional work in <em>car vinyl wraps</em>, wall graphics and signage. We take pride in having the best designers and installers nationwide.</p>
</section>

<section class="section promo">
  <h2 class="abs">NO INTEREST. NO PAYMENTS<br>FOR 3 MONTHS.</h2>
  <div class="abs btn promo-btn">Book Now</div>
  <div class="abs promo-art" role="img" aria-label="Photo of a red and white wrapped hatchback, side view"></div>
</section>

<section class="section gallery">
  <h2 class="abs">GALLERY</h2>
  <div class="abs gallery-grid">
    <div class="shot g1" role="img" aria-label="Service van with a heating company wrap"></div>
    <div class="shot g2" role="img" aria-label="Pickup truck with a graphic wrap"></div>
    <div class="shot g3" role="img" aria-label="Wrapped work van with purple graphics"></div>
    <div class="shot g4" role="img" aria-label="Black sedan with a gloss wrap at sunset"></div>
    <div class="shot g5" role="img" aria-label="White car with blue stripe livery in snow"></div>
    <div class="shot g6" role="img" aria-label="Plumbing company box truck with green and blue wrap"></div>
    <div class="shot g7" role="img" aria-label="Matte black coupe front in a workshop"></div>
    <div class="shot g8" role="img" aria-label="Satin black sedan in a garage bay"></div>
  </div>
</section>

<section class="section contact">
  <div class="abs contact-card">
    <h2>CONTACT US</h2>
    <div class="field" style="left:38px;top:106px;width:176px">First Name</div>
    <div class="field" style="left:226px;top:106px;width:178px">Last Name</div>
    <div class="field" style="left:38px;top:166px;width:176px">Email</div>
    <div class="field" style="left:226px;top:166px;width:178px">Phone</div>
    <div class="field" style="left:38px;top:236px;width:366px;height:88px">Message</div>
    <div class="btn send-btn">Send</div>
    <div class="contact-photo" role="img" aria-label="Customer service agent on a phone call at a laptop"></div>
  </div>
</section>

<footer class="section site-footer">
  <div class="abs brand footer-brand"><span class="mark"></span><span>BRIGHT COAT<br>STUDIO</span></div>
  <div class="abs socials" aria-label="Social links"><i></i><i></i><i></i></div>
  <p class="abs copy">© 2025 Bright Coat Studio. All rights reserved.</p>
  <div class="abs fcol" style="left:418px">
    <h3>Top Services</h3>
    <ul><li>Vinyl Wraps</li><li>Clear Shield Protection Film</li><li>Matte Paint Protection Film</li><li>Coloured PPF</li><li>Ceramic Coating</li><li>Car Detailing</li><li>Custom Decals</li></ul>
  </div>
  <div class="abs fcol" style="left:653px">
    <h3>Useful Links</h3>
    <ul><li>About</li><li>Services</li><li>Promotions</li><li>Gallery</li><li>Contact Us</li></ul>
  </div>
  <div class="abs fcol" style="left:861px">
    <h3>Contact</h3>
    <ul>
      <li class="ico"><svg width="11" height="11" viewBox="0 0 12 12"><path d="M2.5 .5l2 2.5-1.2 1.5a7 7 0 0 0 4.2 4.2L9 7.5l2.5 2-1.2 2C5 11.5.5 7 .5 1.7z" fill="#3b9af0"/></svg>+800-5210-3388</li>
      <li class="ico"><svg width="12" height="10" viewBox="0 0 13 10"><rect width="13" height="10" rx="1.5" fill="#3b9af0"/><path d="M1 1.5l5.5 4 5.5-4" stroke="#18181b" stroke-width="1.2" fill="none"/></svg>info@brightcoatstudio.com</li>
      <li class="ico"><svg width="10" height="13" viewBox="0 0 10 13"><path d="M5 0a5 5 0 0 1 5 5c0 3.5-5 8-5 8S0 8.5 0 5a5 5 0 0 1 5-5z" fill="#3b9af0"/><circle cx="5" cy="5" r="1.8" fill="#18181b"/></svg>12 Lantern Row, Fenwick Park,<br>Ostrava Bay</li>
    </ul>
  </div>
</footer>

</body>
</html>
```